Hillcrest BBQ Co. Rub and Sauce Labels

I am bringing to market 3 different meat rubs and 2 BBQ sauces. These rubs and sauces will be sold on an eCommerce website and also at local events. I am looking for simplicity. I believe the BBQ seasoning labels out there are very busy. I am looking for each label to be similar, yet distinct enough to clearly differentiate the different rubs in my offerings. My logo is attached. The Smoky H in my logo is going to be a feature in my brand and would like to have it be a feature on my labels, too. The rubs will be packaged in a traditional clear plastic shaker with a pop-top. I am open to ideas on packaging options as well. The different rubs in the shakers will range in color from very light to dark brown, depending on the ingredients in each rub. Please include all FDA required information on the labels. The rub labels will go on a clear plastic shaker and the sauce will be packaged in a bottle. Thanks for your help and I look forward to seeing your creativity come to life!

Colors

Designer to choose colors to be used in the design.

Requirements
Must have
• Simplicity, yet ability to separate multiple products by simple changes in logo and/or packaging. Please see the attached photo of a competitors bbq sauce - something simple yet flexible.
Nice to have
• Flexibility in design.

```html
<!DOCTYPE html>
<html lang="en">
<head>
<meta charset="utf-8">
<title>Hillcrest BBQ Co. – Rub Labels</title>
<link href="https://fonts.googleapis.com/css2?family=Alfa+Slab+One&family=Archivo+Black&family=Archivo:wght@400;500&family=Roboto+Condensed:wght@400&display=swap" rel="stylesheet">
<style>
  :root {
    --page: #ffffff;
    --strip-light: #ffffff;
    --strip-shade: #e6e6e6;
    --carolina: #13245a;
    --carolina-deep: #0c1a45;
    --carolina-tint: #8c9fd6;
    --smoky: #842a22;
    --smoky-deep: #5a1713;
    --smoky-tint: #e0a7a0;
    --coffee: #5a2418;
    --coffee-deep: #33120c;
    --coffee-tint: #c9a49c;
    --flame-top: #e8202a;
    --flame-mid: #ee5a26;
    --flame-bottom: #f58a22;
    --ink-light: #ffffff;
    --ink-dark: #1f1f1f;
  }
  * { box-sizing: border-box; margin: 0; padding: 0; }
  html, body { width: 1200px; height: 1200px; overflow: hidden; background: var(--page); }
  .label-row {
    position: absolute; left: 47px; top: 427px;
    display: flex; gap: 28px;
  }
  .label {
    position: relative; width: 350px; height: 345px; overflow: hidden;
    background: linear-gradient(90deg, var(--strip-light) 0, var(--strip-shade) 125px, var(--panel) 125px, var(--panel-deep) 100%);
  }
  .label--carolina { --panel: var(--carolina); --panel-deep: var(--carolina-deep); --tint: var(--carolina-tint); }
  .label--smoky    { --panel: var(--smoky);    --panel-deep: var(--smoky-deep);    --tint: var(--smoky-tint); }
  .label--coffee   { --panel: var(--coffee);   --panel-deep: var(--coffee-deep);   --tint: var(--coffee-tint); }

  .brand {
    position: absolute; left: 10px; top: 22px; width: 110px;
    display: flex; flex-direction: column; align-items: center; gap: 6px;
  }
  .brand-dot { width: 16px; height: 16px; border-radius: 50%; background: var(--flame-mid); }
  .brand-name {
    font-family: "Archivo", sans-serif; font-weight: 500; font-size: 10px;
    color: var(--ink-dark); text-align: center; line-height: 1.2;
  }
  .flame-art {
    position: absolute; left: 0; top: 95px; width: 155px; height: 250px;
    border-radius: 0 150px 0 0;
    background: linear-gradient(180deg, var(--flame-top) 0%, var(--flame-mid) 45%, var(--flame-bottom) 100%);
  }
  .title {
    position: absolute; left: 150px; right: 0; text-align: center;
  }
  .flavor {
    top: 22px; font-family: "Archivo", sans-serif; font-weight: 400;
    font-size: 31px; color: var(--tint); letter-spacing: 0.5px;
  }
  .bbq {
    top: 58px; font-family: "Alfa Slab One", serif; font-size: 54px;
    color: var(--ink-light); line-height: 1; letter-spacing: 1px;
  }
  .rub {
    top: 120px; font-family: "Archivo Black", sans-serif; font-size: 32px;
    color: var(--ink-light); letter-spacing: 4px; line-height: 1;
  }
  .rule {
    position: absolute; left: 168px; right: 0; top: 170px;
    height: 1.5px; background: var(--ink-light); opacity: 0.85;
  }
  .description {
    position: absolute; left: 168px; width: 176px; top: 185px;
    font-family: "Archivo", sans-serif; font-size: 11.5px; line-height: 15px;
    color: var(--ink-light); white-space: nowrap;
  }
  .net-weight {
    position: absolute; right: 18px; bottom: 18px;
    font-family: "Roboto Condensed", sans-serif; font-size: 12.5px;
    color: var(--ink-light);
  }
</style>
</head>
<body>
  <main class="label-row">
    <section class="label label--carolina">
      <div class="flame-art" role="img" aria-label="Large red-to-orange flame swoosh brand graphic"></div>
      <div class="brand"><span class="brand-dot"></span><span class="brand-name">Hillcrest BBQ Co.</span></div>
      <p class="title flavor">CAROLINA</p>
      <p class="title bbq">BBQ</p>
      <p class="title rub">RUB</p>
      <div class="rule"></div>
      <p class="description">Lorem Ipsum. Proin gravida<br>nibh vel velit auctor aliquet.<br>Aenean sollicitudin, lorem<br>quis bibendum auctor, nisi elit<br>consequat ipsum, nec sagittis<br>sem nibh id elit.</p>
      <p class="net-weight">Net Wt. 20 oz (1.25 lbs.)</p>
    </section>
    <section class="label label--smoky">
      <div class="flame-art" role="img" aria-label="Large red-to-orange flame swoosh brand graphic"></div>
      <div class="brand"><span class="brand-dot"></span><span class="brand-name">Hillcrest BBQ Co.</span></div>
      <p class="title flavor">SMOKY</p>
      <p class="title bbq">BBQ</p>
      <p class="title rub">RUB</p>
      <div class="rule"></div>
      <p class="description">Lorem Ipsum. Proin gravida<br>nibh vel velit auctor aliquet.<br>Aenean sollicitudin, lorem<br>quis bibendum auctor, nisi elit<br>consequat ipsum, nec sagittis<br>sem nibh id elit.</p>
      <p class="net-weight">Net Wt. 20 oz (1.25 lbs.)</p>
    </section>
    <section class="label label--coffee">
      <div class="flame-art" role="img" aria-label="Large red-to-orange flame swoosh brand graphic"></div>
      <div class="brand"><span class="brand-dot"></span><span class="brand-name">Hillcrest BBQ Co.</span></div>
      <p class="title flavor">COFFEE</p>
      <p class="title bbq">BBQ</p>
      <p class="title rub">RUB</p>
      <div class="rule"></div>
      <p class="description">Lorem Ipsum. Proin gravida<br>nibh vel velit auctor aliquet.<br>Aenean sollicitudin, lorem<br>quis bibendum auctor, nisi elit<br>consequat ipsum, nec sagittis<br>sem nibh id elit.</p>
      <p class="net-weight">Net Wt. 20 oz (1.25 lbs.)</p>
    </section>
  </main>
</body>
</html>
```